a residential cleaning service needs a website

We need a website for our faith based residential cleaning service, we are called MARGOT'S CLEANING SERVICE. We want a website that is clean looking both for mobile version and desktop. We want to convey cleanliness and trust to our clients. The color scheme should go in hand with the colors of the LOGO. We would like an about page, statement of faith page, services page and also a page for a booking module that our CRM has provided for us to being able to code and dress said module is important. The website not only needs to market to new customers and convey our service but also be easy to use for existing clients to schedule cleanings and services.
Industry/Entity Type
Cleaning Service
Coding
Coded - Design and coding required
Number of Pages Required
4 page
Requirements
Must have
- About page
Statement of Faith page
services page
booking and login page

```html
<!DOCTYPE html>
<html lang="en">
<head>
<meta charset="utf-8">
<title>Statement of Faith – Margot's Cleaning Service</title>
<link href="https://fonts.googleapis.com/css2?family=Cinzel:wght@400;600&family=Poppins:ital,wght@0,400;0,500;0,600;1,600;1,700&display=swap" rel="stylesheet">
<style>
:root{
  --brand-blue:#24489a;
  --brand-blue-dark:#1d3d86;
  --hero-blue:#4f6fb3;
  --slate:#545556;
  --ink:#1f1f22;
  --nav-ink:#4a4a4a;
  --footer-navy:#13284c;
  --footer-line:#2f4670;
  --social-bg:#2a3d60;
  --social-ink:#8f9bb3;
  --white:#ffffff;
  --star:#f4cf63;
}
*{box-sizing:border-box;margin:0;padding:0}
html,body{width:823px;height:1200px;overflow:hidden;background:var(--white)}
body{position:relative;font-family:'Poppins',sans-serif;color:var(--ink)}
.abs{position:absolute}

/* header */
.site-header{position:absolute;left:0;top:0;width:823px;height:60px;background:var(--white);z-index:3}
.main-nav{position:absolute;top:27px;left:0;font-size:6.8px;font-weight:600;letter-spacing:.1px}
.main-nav a{position:absolute;white-space:nowrap;color:var(--nav-ink);text-decoration:none;text-transform:uppercase}
.main-nav a.is-current{color:var(--brand-blue)}
.login-btn{position:absolute;left:602px;top:21px;width:60px;height:21px;border-radius:11px;background:var(--brand-blue);color:var(--white);font-size:6.8px;font-weight:600;display:flex;align-items:center;justify-content:center;gap:5px}
.brand-badge{position:absolute;left:161px;top:1px;width:116px;height:112px;border-radius:50%;background:var(--white);display:flex;align-items:center;justify-content:center;text-align:center;z-index:4}
.brand-badge span{font-family:'Cinzel',serif;font-weight:600;color:var(--brand-blue);font-size:11px;line-height:1.25}

/* hero */
.hero{position:absolute;left:0;top:60px;width:823px;height:240px}
.hero-photo{position:absolute;left:0;top:0;width:823px;height:210px;background:linear-gradient(100deg,#5473b6 0%,#4a68ad 45%,#6381bf 100%)}
.hero-title{position:absolute;left:0;width:823px;top:62px;text-align:center;font-family:'Cinzel',serif;font-weight:400;font-size:34px;letter-spacing:1.5px;color:var(--white)}
.breadcrumb{position:absolute;left:0;width:823px;top:108px;text-align:center;color:var(--white);font-size:9px;font-weight:500}
.breadcrumb .sep{margin:0 9px;font-size:8px}
.hero-curves{position:absolute;left:0;top:0}

/* content */
.section-title{font-family:'Cinzel',serif;font-weight:400;color:var(--brand-blue);font-size:25px;line-height:26px;letter-spacing:.6px}
.rule{width:30px;height:1.5px;background:var(--slate)}
.body-copy{font-size:7px;line-height:12px;color:var(--ink)}
.faith-portrait{position:absolute;left:180px;top:338px;width:234px;height:234px;border-radius:50%;background:radial-gradient(circle at 35% 40%,#f1d9c4 0%,#b8d8d0 45%,#7fcfbf 70%,#e8c78f 100%)}

/* footer */
.site-footer{position:absolute;left:0;top:896px;width:823px;height:304px;background:radial-gradient(circle at 8% 30%,#1b3562 0%,transparent 30%),radial-gradient(circle at 92% 70%,#1b3562 0%,transparent 30%),var(--footer-navy);color:var(--white)}
.social-dot{position:absolute;top:29px;width:20px;height:20px;border-radius:50%;background:var(--social-bg);color:var(--social-ink);font-size:5.5px;font-weight:500;display:flex;align-items:center;justify-content:center}
.newsletter{position:absolute;left:424px;top:24px;width:238px;height:31px;border-radius:16px;background:var(--white)}
.newsletter .field{position:absolute;left:33px;top:9px;font-size:8.5px;color:#9aa3b3}
.newsletter .mail-ico{position:absolute;left:17px;top:11px}
.subscribe-btn{position:absolute;right:4px;top:4px;width:84px;height:24px;border-radius:12px;background:var(--brand-blue);color:var(--white);font-size:9px;font-weight:600;display:flex;align-items:center;justify-content:center}
.footer-rule{position:absolute;left:161px;width:501px;height:1px;background:var(--footer-line)}
.footer-brand{position:absolute;left:180px;top:102px;width:120px;text-align:center;font-family:'Cinzel',serif;font-weight:600;font-size:11px;line-height:1.3;color:var(--white)}
.footer-about{position:absolute;left:160px;top:199px;width:160px;text-align:center;font-size:7.2px;line-height:12px}
.footer-heading{position:absolute;top:108px;font-family:'Cinzel',serif;font-weight:400;font-size:12.5px;letter-spacing:.5px}
.footer-links a{position:absolute;font-size:7.2px;color:var(--white);text-decoration:none;white-space:nowrap}
.contact-line{position:absolute;left:505px;font-size:7.2px;line-height:10px;display:flex;gap:6px}
.copyright{position:absolute;left:0;width:823px;top:277px;text-align:center;font-size:6.2px;color:#c9d0dd}
</style>
</head>
<body>

<header class="site-header">
  <nav class="main-nav">
    <a href="#" style="left:313px">Home</a>
    <a href="#" style="left:355px">About</a>
    <a href="#" class="is-current" style="left:400px">Statement of Faith</a>
    <a href="#" style="left:492px">Services</a>
    <a href="#" style="left:547px">Booking</a>
  </nav>
  <div class="login-btn">
    <svg width="10" height="10" viewBox="0 0 10 10" fill="none" stroke="#fff" stroke-width="0.9"><circle cx="5" cy="3.2" r="2.2"/><path d="M1 9.5c0-2.3 1.8-3.6 4-3.6s4 1.3 4 3.6"/></svg>
    LOGIN
  </div>
</header>
<div class="brand-badge"><span>MARGOT'S<br>CLEANING<br>SERVICE</span></div>

<section class="hero">
  <div class="hero-photo" role="img" aria-label="Cleaners in blue uniforms mopping and wiping a room, tinted blue"></div>
  <svg class="hero-curves" width="823" height="240" viewBox="0 60 823 240">
    <path d="M0,180 Q400,330 823,190 L823,300 L0,300 Z" fill="#545556"/>
    <path d="M0,210 Q420,335 750,243 Q800,232 823,226 L823,300 L0,300 Z" fill="#ffffff"/>
    <path d="M80,207 Q430,306 823,181 L823,212 Q430,320 80,207 Z" fill="#24489a"/>
    <path d="M70,204 Q430,300 823,177" fill="none" stroke="#ffffff" stroke-width="1.6"/>
  </svg>
  <h1 class="hero-title">STATEMENT OF FAITH</h1>
  <div class="breadcrumb">Home<span class="sep">&gt;</span>Statement of Faith</div>
</section>

<svg class="abs" style="left:323px;top:294px" width="16" height="16" viewBox="0 0 16 16"><path d="M8 1 Q9 7 15 8 Q9 9 8 15 Q7 9 1 8 Q7 7 8 1Z" fill="none" stroke="#f4cf63" stroke-width="1.3"/></svg>

<svg class="abs" style="left:150px;top:310px" width="300" height="290" viewBox="150 310 300 290">
  <path d="M164,471 L164,455 A133,133 0 0 1 382,353" fill="none" stroke="#545556" stroke-width="11"/>
  <path d="M255,337 A125,125 0 0 1 422,455 L422,471" fill="none" stroke="#24489a" stroke-width="6"/>
  <path d="M192,537 A133,133 0 0 0 371,566" fill="none" stroke="#545556" stroke-width="9"/>
  <path d="M225,558 A125,125 0 0 0 393,535" fill="none" stroke="#24489a" stroke-width="5"/>
</svg>
<div class="faith-portrait" role="img" aria-label="Smiling cleaner in an apron holding a caddy of cleaning supplies and a rainbow duster"></div>

<h2 class="section-title abs" style="left:465px;top:367px">STATEMENT OF<br>FAITH</h2>
<div class="rule abs" style="left:463px;top:422px"></div>
<p class="body-copy abs" style="left:463px;top:438px;width:204px">As a faith based business Margot’s Cleaning Service clings to <b><i>Colossians 3:23 “ And whatsoever &nbsp;ye do, do it heartily as to The Lord and not unto men.”</i></b> &nbsp;Therefore every job that we do we as a business we pray that the job we perform is pleasing to God. Not only do we see every job as an opportunity to glorify God, but we see every client as a member of the family and look for opportunities to show love and be a light in a dark world.</p>

<h2 class="section-title abs" style="left:162px;top:628px">HIGHLY TRAINED, AND SCREENED<br>EMPLOYEES</h2>
<div class="rule abs" style="left:161px;top:688px"></div>
<p class="body-copy abs" style="left:161px;top:704px;width:506px">Our professional house cleaners are held to very high standards not only in cleaning, but social performance as well. Starting with an extensive screening process including background checks and testing moral character, we then train every qualified candidate to have an eye for detail and be an absolute delight to have in anyone’s presence.</p>

<h2 class="section-title abs" style="left:162px;top:769px">SURPRISINGLY AFFORDABLE</h2>
<div class="rule abs" style="left:161px;top:803px"></div>
<p class="body-copy abs" style="left:161px;top:819px;width:506px">At Margot’s Cleaning Service we are often able to offer our high quality cleaning services at lower cost than our big company competitors. Although many of our clients have switched their cleaning service provider to ours based on performance, they are often surprised to find that they save money as well!</p>

<footer class="site-footer">
  <span class="social-dot" style="left:161px">Pix</span>
  <span class="social-dot" style="left:190px">Zed</span>
  <span class="social-dot" style="left:219px">Kup</span>
  <span class="social-dot" style="left:248px">Vu</span>

  <div class="newsletter">
    <svg class="mail-ico" width="11" height="9" viewBox="0 0 11 9" fill="none" stroke="#8a94a6" stroke-width="0.9"><rect x="0.5" y="0.5" width="10" height="6.5" rx="1"/><path d="M3 3h5M3 5h3"/></svg>
    <span class="field">Email</span>
    <div class="subscribe-btn">Subscribe</div>
  </div>

  <div class="footer-rule" style="top:78px"></div>

  <div class="footer-brand">MARGOT'S<br>CLEANING<br>SERVICE</div>
  <p class="footer-about">Margot’s Cleaning Service is a faith based cleaning business founded in middle Tennessee over 19 years ago.</p>

  <h3 class="footer-heading" style="left:332px">QUICK LINKS</h3>
  <div class="footer-links">
    <a href="#" style="left:332px;top:138px">About</a>
    <a href="#" style="left:332px;top:155px">Statement of Faith</a>
    <a href="#" style="left:332px;top:172px">Services</a>
    <a href="#" style="left:332px;top:189px">Booking</a>
    <a href="#" style="left:332px;top:206px">Contact</a>
    <a href="#" style="left:422px;top:138px">Conditions</a>
    <a href="#" style="left:422px;top:155px">Terms of Use</a>
    <a href="#" style="left:422px;top:172px">Privacy</a>
  </div>

  <h3 class="footer-heading" style="left:505px">LET’S TALK</h3>
  <div class="contact-line" style="top:139px">
    <svg width="7" height="8" viewBox="0 0 7 8"><path d="M1.2 0.5 L2.6 0.5 L3 2.3 L2.1 3 Q2.8 4.6 4.2 5.4 L4.9 4.5 L6.6 5 L6.6 6.6 Q3.6 7.4 1.4 4.6 Q0 2.6 1.2 0.5Z" fill="#3f66c4"/></svg>
    <span>+00 555 014 782</span>
  </div>
  <div class="contact-line" style="top:158px">
    <svg width="7" height="8" viewBox="0 0 7 8"><rect x="0" y="1.5" width="7" height="5" rx="0.6" fill="#3f66c4"/><path d="M0.4 2 L3.5 4.3 L6.6 2" fill="none" stroke="#13284c" stroke-width="0.6"/></svg>
    <span>hello@margotscleaningservice.com</span>
  </div>
  <div class="contact-line" style="top:177px">
    <svg width="7" height="9" viewBox="0 0 7 9"><path d="M3.5 0.5 A3 3 0 0 1 6.5 3.5 Q6.5 5.5 3.5 8.5 Q0.5 5.5 0.5 3.5 A3 3 0 0 1 3.5 0.5Z" fill="#3f66c4"/><circle cx="3.5" cy="3.4" r="1" fill="#13284c"/></svg>
    <span>PO Box 41210 Elm st. 212,<br>Riverside, California, Us.</span>
  </div>

  <div class="footer-rule" style="top:258px"></div>
  <p class="copyright">Copyright © &nbsp;2020 MARGOT’S CLEANING SERVICE. All Rights Reserved</p>
</footer>

</body>
</html>
```